Mortgage Loan officer needs clean/modern business card design

Looking for a clean, modern 2-sided business card design. We like the earth tones used in our logo and website http://varnhill-lending.com . Would also like to incorporate: 1) Something special to make our card stand out - a pop of color or embossed logo, for instance and 2) please include "Mortgage Loans" "Reverse Mortgages" "Private Money Loans" on back of card with the logo.

Front: Needs to include agent/company license info - see website. Agent name: Marco Lindqvist

Here are fonts and colors used for our logo:
Font: Avenir Next
Colors:
#2c3539 - Dark Gray
#576870 - Light Gray
#ffffff - Background White

Target Market(s)

Prospects and current clients. Will also be distributing to people in professional network (attorneys and CPAs)

Industry/Entity Type

Business

Contact Information for Business Card

Include agent name, contact info, website on front, licensing info for agent an company. Logo and services offered on back

Font styles to use
Other font styles liked:
• Avenir Next

Requirements
Must have
• See project description
Should not have
• Nothing cheesy

```html
<!DOCTYPE html>
<html lang="en">
<head>
<meta charset="UTF-8">
<title>Varnhill Lending – Business Card</title>
<link href="https://fonts.googleapis.com/css2?family=Nunito+Sans:wght@400;600;700&display=swap" rel="stylesheet">
<style>
  :root {
    --dark-gray: #2c3539;
    --light-gray: #576870;
    --card-white: #ffffff;
    --backdrop: #e9eaeb;
    --rule: #9aa4a9;
  }
  * { box-sizing: border-box; margin: 0; padding: 0; }
  html, body { width: 1200px; height: 747px; overflow: hidden; }
  body {
    background: var(--backdrop);
    font-family: "Nunito Sans", "Avenir Next", sans-serif;
    color: var(--dark-gray);
    position: relative;
  }
  .card {
    position: absolute;
    top: 219px;
    width: 540px;
    height: 309px;
    background: var(--card-white);
    box-shadow: 0 2px 10px rgba(44,53,57,0.12);
  }
  .card--back { left: 40px; }
  .card--front { left: 620px; }

  .brand-mark {
    width: 130px;
    height: 130px;
    border: 1.5px solid var(--rule);
    border-radius: 50%;
    display: flex;
    align-items: center;
    justify-content: center;
    text-align: center;
    font-size: 15px;
    font-weight: 600;
    line-height: 1.2;
    color: var(--light-gray);
    padding: 0 18px;
  }
  .card--back .brand-mark { position: absolute; left: 205px; top: 38px; }
  .card--front .brand-mark { position: absolute; right: 36px; top: 30px; width: 104px; height: 104px; font-size: 12px; }

  .website {
    position: absolute;
    top: 190px;
    width: 100%;
    text-align: center;
    font-size: 15px;
    font-weight: 700;
    color: var(--light-gray);
  }
  .services {
    position: absolute;
    bottom: 30px;
    width: 100%;
    text-align: center;
    font-size: 13px;
    font-weight: 700;
    letter-spacing: 0.3px;
    text-transform: uppercase;
    color: var(--light-gray);
  }
  .services .sep { margin: 0 10px; font-weight: 400; }

  .agent { position: absolute; left: 34px; top: 112px; }
  .agent-name { font-size: 22px; font-weight: 400; color: var(--dark-gray); }
  .agent-title, .agent-license { font-size: 13px; color: var(--light-gray); line-height: 1.35; }
  .license-numbers { font-size: 10.5px; font-weight: 700; color: var(--dark-gray); margin-top: 2px; }

  .contact-list {
    position: absolute;
    left: 34px;
    top: 196px;
    list-style: none;
    font-size: 12px;
    color: var(--light-gray);
    line-height: 1.45;
  }
  .contact-list li { display: flex; align-items: flex-start; }
  .contact-list svg { width: 11px; height: 11px; margin: 3px 9px 0 0; flex: none; fill: var(--light-gray); }
</style>
</head>
<body>
  <section class="card card--back" aria-label="Card back">
    <div class="brand-mark">The Lindqvist Group</div>
    <p class="website">varnhill-lending.com</p>
    <p class="services">Mortgage Loans<span class="sep">|</span>Reverse Mortgages<span class="sep">|</span>Private Money Loans</p>
  </section>

  <section class="card card--front" aria-label="Card front">
    <div class="brand-mark">The Lindqvist Group</div>
    <div class="agent">
      <h1 class="agent-name">Marco Lindqvist</h1>
      <p class="agent-title">Loan Officer</p>
      <p class="agent-license">Fed and State License</p>
      <p class="license-numbers">NMLS:406215 DRE:02718436 CO: DRE:01592073/NMLS:517284</p>
    </div>
    <ul class="contact-list">
      <li><svg viewBox="0 0 12 12"><path d="M1 4c0-2 2-3 5-3s5 1 5 3l-2 1-1-2H4L3 5zM2 6h8l1 5H1z"/></svg>408-555-0170 x214</li>
      <li><svg viewBox="0 0 12 12"><path d="M3 0h6v12H3zM4 1.5v8h4v-8z"/></svg>650-555-0142</li>
      <li><svg viewBox="0 0 12 12"><path d="M3 0h6v4H3zM1 5h10v6H1zM3 7v2h6V7z"/></svg>408-555-0188</li>
      <li><svg viewBox="0 0 12 12"><path d="M0 2h12v8H0zM1 3l5 4 5-4z" fill-rule="evenodd"/></svg>marco@varnhill-lending.com</li>
      <li><svg viewBox="0 0 12 12"><path d="M6 0a4 4 0 0 1 4 4c0 3-4 8-4 8S2 7 2 4a4 4 0 0 1 4-4zm0 2.5a1.5 1.5 0 1 0 0 3 1.5 1.5 0 0 0 0-3z"/></svg>2180 Orchard Row, Suite 305<br>Maple Hollow, CA 95000</li>
    </ul>
  </section>
</body>
</html>
```